Colocation Data Center Web Site

Would be to design a specialized site specifically for a Data Center that provide colocation services to their clients.
This site would need to have a client portal to allow them to see the status of their bills, list of services and to create service tickets.

Industry/Entity Type

It Service

```html
<!DOCTYPE html>
<html lang="en">
<head>
<meta charset="utf-8">
<title>Heronvault — Colocation Services</title>
<link href="https://fonts.googleapis.com/css2?family=Montserrat:wght@400;600;700;800&family=Arimo:wght@400;700&display=swap" rel="stylesheet">
<style>
:root{
  --navy:#3b4a8a;
  --navy-dark:#333e6c;
  --orange:#f0661c;
  --ink:#4a4a4a;
  --muted:#7a7a7a;
  --panel:#e9e9eb;
  --band:#5d5a5e;
  --white:#fff;
}
*{margin:0;padding:0;box-sizing:border-box}
html,body{width:907px;height:1200px;overflow:hidden;background:#fff}
body{position:relative;font-family:"Arimo",Arial,sans-serif;color:var(--ink)}
.abs{position:absolute}
.head-font{font-family:"Montserrat",Arial,sans-serif}

.site-header{left:0;top:0;width:907px;height:78px;background:linear-gradient(#fff,#ececee);border-bottom:2px solid #dcdcdf}
.brand{left:152px;top:30px;display:flex;align-items:center;gap:6px;font-family:"Montserrat",sans-serif;font-weight:700;font-size:13px;letter-spacing:1.5px;color:var(--navy-dark)}
.brand i{width:12px;height:12px;border-radius:50%;background:var(--navy)}
.top-links{left:496px;top:13px;font-size:11px;font-weight:700;color:#555;display:flex;gap:12px;align-items:center}
.top-links .login{color:var(--navy)}
.top-links .sep{color:#bbb;font-weight:400}
.top-links .phone{font-weight:400;color:#999;font-size:12px;display:flex;gap:4px;align-items:center}
.main-nav{left:422px;top:48px;display:flex;align-items:center;font-size:9.5px;color:#555;letter-spacing:.2px}
.main-nav a{padding:0 9px;border-right:1px dotted #aaa;text-decoration:none;color:inherit}
.main-nav a:last-child{border:0}
.main-nav .active{background:linear-gradient(#6c7ab3,#4a5891);color:#fff;height:18px;line-height:18px;border:0;padding:0 9px;border-radius:1px}

.hero{left:0;top:80px;width:907px;height:348px;background:linear-gradient(#fff 0%,#e4e4e6 80%,#fff 81%)}
.hero-kicker{left:201px;top:108px;font-size:22px;font-weight:700;color:#555;letter-spacing:-.5px}
.hero-title{left:201px;top:126px;font-weight:800;font-size:31px;color:var(--navy);letter-spacing:-1.5px;white-space:nowrap}
.hero-title small{font-size:21px;color:#555;letter-spacing:-1px}
.btn{display:flex;align-items:center;justify-content:center;color:#fff;font-family:"Montserrat",sans-serif;font-weight:600;letter-spacing:-.4px;border-radius:2px}
.btn-orange{background:linear-gradient(#f78a3a,var(--orange));}
.btn-navy{background:linear-gradient(#6d7bbb,#48579a)}
.hero-media{left:152px;top:200px;width:600px;height:224px;background:linear-gradient(90deg,#6a6b70,#3a3b40 30%,#8e9096 55%,#2c2d31 75%,#c9ccd3);border-radius:3px;opacity:.85}

.welcome-title{left:152px;top:450px;font-size:20px;font-weight:800;color:var(--navy);letter-spacing:-1px}
.welcome-text{left:152px;top:476px;width:604px;font-size:7.6px;line-height:10.2px;color:#555}
.read-more{left:680px;top:523px;width:76px;text-align:right;font-size:7.5px;font-weight:700;color:var(--navy)}
.dash{left:190px;width:526px;border-top:1px dashed #cfcfd3}

.tab{top:574px;height:25px;display:flex;align-items:center;justify-content:center;font-family:"Montserrat",sans-serif;font-size:11px;font-weight:600;letter-spacing:-.6px}
.tab-light{left:152px;width:114px;background:var(--panel);color:var(--navy)}
.tab-dark{left:267px;width:107px;background:#5f5a62;color:#fff;height:22px;box-shadow:3px 3px 0 #cfcfd2}
.plan-panel{left:152px;top:599px;width:604px;height:178px;background:var(--panel);border-radius:0 3px 3px 3px}
.cabinet-media{left:162px;top:624px;width:78px;height:86px;background:linear-gradient(90deg,#2a2a2e,#6d6e73,#1e1e22);border-radius:2px}
.plan{top:630px;width:100px;text-align:center}
.plan .unit{margin:0 auto;background:linear-gradient(#59595f,#2c2c30);border-radius:1px}
.plan .u{position:absolute;left:0;width:100px;top:74px;font-family:"Montserrat",sans-serif;font-weight:600;font-size:24px;color:var(--navy)}
.plan .price{position:absolute;left:0;width:100px;top:104px;font-family:"Montserrat",sans-serif;font-size:16px;color:#666;letter-spacing:-.6px}
.vsep{top:688px;height:72px;border-left:1px dashed #c8c8cc}

.park-title{left:0;top:858px;width:907px;text-align:center;font-size:19px;font-weight:800;color:var(--navy);letter-spacing:-.9px}
.park-text{left:152px;top:885px;width:604px;text-align:center;font-size:10.4px;line-height:13.5px;color:#555}

.col-title{top:979px;font-size:14px;font-weight:700;color:var(--navy);letter-spacing:-.8px}
.link-list{top:1008px;list-style:none;font-size:9px;color:#555}
.link-list li{height:17.5px;display:flex;align-items:center;gap:6px}
.link-list li::before{content:"";width:7px;height:7px;border-radius:50%;border:1px solid #aaa;background:#eee}
.vline{border-left:1px dashed #d3d3d6}
.news{top:1009px;width:118px;font-size:7.6px;line-height:10.5px;color:#555}
.news b{display:block;color:#444;margin-bottom:2px}
.news .more{display:block;text-align:right;color:var(--navy);font-weight:700;margin-top:6px}

.social-band{left:0;top:1086px;width:907px;height:31px;background:repeating-linear-gradient(135deg,#615e62 0 2px,#575458 2px 4px)}
.social-text{left:153px;top:1093px;font-family:"Montserrat",sans-serif;font-weight:700;font-size:13px;color:#fff;letter-spacing:-.6px;display:flex;gap:5px;align-items:center}
.social-text i{width:18px;height:18px;border-radius:50%;background:#fff;display:inline-block;margin-left:1px}

.site-footer{left:0;top:1118px;width:907px;height:82px;background:var(--navy-dark)}
.foot-col{top:1133px;color:#e6e8f2;font-size:7.8px;line-height:12px}
.foot-col h3{font-family:"Montserrat",sans-serif;font-size:14px;font-weight:700;color:#fff;letter-spacing:-.3px;margin-bottom:3px}
.foot-sep{top:1138px;height:46px;border-left:1px dashed #56619a}
.foot-brand{left:664px;top:1138px;display:flex;align-items:center;gap:5px;font-family:"Montserrat",sans-serif;font-weight:700;font-size:11px;letter-spacing:1px;color:#cfd3e6}
.foot-brand i{width:10px;height:10px;border-radius:50%;background:#cfd3e6}
.copyright{left:654px;top:1166px;font-size:8px;line-height:10.5px;color:#c8cce0}
</style>
</head>
<body>

<header class="site-header abs"></header>
<div class="brand abs"><i></i>HERONVAULT</div>
<div class="top-links abs">
  <span class="login">LOGIN</span><span class="sep">|</span><span>REGISTER</span><span class="sep">|</span>
  <span class="phone"><svg width="10" height="10" viewBox="0 0 24 24"><path fill="#4a5891" d="M6.6 10.8a15 15 0 0 0 6.6 6.6l2.2-2.2c.3-.3.7-.4 1-.2 1.1.4 2.3.6 3.6.6.6 0 1 .4 1 1V20c0 .6-.4 1-1 1A17 17 0 0 1 3 4c0-.6.4-1 1-1h3.5c.6 0 1 .4 1 1 0 1.3.2 2.5.6 3.6.1.3 0 .7-.2 1z"/></svg>800.555.0142 (0142)</span>
</div>
<nav class="main-nav abs">
  <a class="active">HOME</a><a>OUR SERVICES</a><a>ABOUT US</a><a>PRODUCTS</a><a>CONTACT US</a>
</nav>

<section class="hero abs"></section>
<div class="hero-kicker abs head-font">PROVIDE</div>
<h1 class="hero-title abs head-font">COLOCATION SERVICES <small>TO THEIR CLIENTS!</small></h1>
<div class="btn btn-orange abs" style="left:502px;top:164px;width:143px;height:26px;font-size:13px">Request a Demo</div>
<div class="btn btn-navy abs" style="left:651px;top:164px;width:105px;height:26px;font-size:13px">Buy Now!</div>
<div class="hero-media abs" role="img" aria-label="Rack servers, a tower server and a monitor showing a management dashboard"></div>

<h2 class="welcome-title abs head-font">WELCOME TO HERONVAULT</h2>
<p class="welcome-text abs">Lorem ipsum dolor sit amet, consectetur adipiscing elit. Fusce hendrerit nibh nec nunc aliquam feugiat. Nam sit amet pellentesque libero. Mauris sem turpis, pulvinar quis sapien in, tempus placerat mauris. Sed posuere et enim in cursus. Donec aliquet sodales sapien, a pellentesque velit euismod at. Nulla orci purus, tempus nec faucibus non, bibendum eu risus. Aliquam euismod lorem vel mi mattis consequat non vel augue. Integer congue dolor id lacinia consequat. Quisque augue est, varius in ornare vel, sollicitudin ut tortor. Cras nec lacinia eros.</p>
<div class="read-more abs">Read More...</div>
<div class="dash abs" style="top:544px"></div>

<div class="tab tab-light abs">Pay-Per-U Colo</div>
<div class="tab tab-dark abs">Private Cabinets</div>
<section class="plan-panel abs"></section>
<div class="cabinet-media abs" role="img" aria-label="Server cabinet"></div>

<div class="plan abs" style="left:249px"><div class="unit" style="width:70px;height:11px;margin-top:34px"></div><div class="u">1U</div><div class="price">$ 75/ mo</div></div>
<div class="plan abs" style="left:354px"><div class="unit" style="width:70px;height:25px;margin-top:27px"></div><div class="u">2U</div><div class="price">$ 99/ mo</div></div>
<div class="plan abs" style="left:452px"><div class="unit" style="width:70px;height:38px;margin-top:20px"></div><div class="u">3U</div><div class="price">$ 115/ mo</div></div>
<div class="plan abs" style="left:553px"><div class="unit" style="width:70px;height:49px;margin-top:14px"></div><div class="u">4U</div><div class="price">$ 125/ mo</div></div>
<div class="plan abs" style="left:657px"><div class="unit" style="width:70px;height:60px;margin-top:9px"></div><div class="u">5U</div><div class="price">$ 129/ mo</div></div>
<div class="vsep abs" style="left:252px"></div>
<div class="vsep abs" style="left:352px"></div>
<div class="vsep abs" style="left:453px"></div>
<div class="vsep abs" style="left:552px"></div>
<div class="vsep abs" style="left:653px"></div>

<div class="btn btn-orange abs" style="left:613px;top:794px;width:143px;height:24px;font-size:10.5px">Customize your Package</div>
<div class="dash abs" style="top:833px"></div>

<h2 class="park-title abs head-font">PARK YOUR SERVERS IN GOOD HANDS WITH COREVANTIS.</h2>
<p class="park-text abs">We offer a wide range of data centre server colocation options &amp; services, including shared small &amp; dedicated cabinets. Server Colocation is the perfect solution if you already own or want to own your own servers &amp; your e-business demands the ultimate in reliability &amp; security</p>
<div class="dash abs" style="top:949px"></div>

<h3 class="col-title abs head-font" style="left:152px">COLOCATION SPACE</h3>
<ul class="link-list abs" style="left:152px"><li>Pay-Per-U &amp; Cabinets</li><li>Cage Leasing</li><li>Hand &amp; Eyes Support</li></ul>
<div class="vline abs" style="left:300px;top:1010px;height:46px"></div>
<ul class="link-list abs" style="left:334px"><li>Point-to Point</li><li>Our Datacenters</li><li>Network Map</li></ul>
<div class="vline abs" style="left:452px;top:990px;height:66px"></div>

<h3 class="col-title abs head-font" style="left:480px">LATES NEWS</h3>
<div class="news abs" style="left:481px"><b>September 5, 2013</b>Lorem ipsum dolor sit amet, consectetur adipiscing elit...<span class="more">More...</span></div>
<div class="vline abs" style="left:618px;top:1012px;height:42px"></div>
<div class="news abs" style="left:638px"><b>September 7, 2013</b>Lorem ipsum dolor sit amet, consectetur adipiscing elit...<span class="more">More...</span></div>

<div class="social-band abs"></div>
<div class="social-text abs">We're Social &nbsp;Follow Us: <i></i><i></i><i></i></div>

<footer class="site-footer abs"></footer>
<div class="foot-col abs" style="left:152px"><h3>CONTACT</h3>Phone: +49 30 555 01 20<br>Telefax: +49 30 555 01 29<br>Email: info@heronvault.example</div>
<div class="foot-sep abs" style="left:303px"></div>
<div class="foot-col abs" style="left:356px"><h3>ABOUT</h3>What we do<br>Insights<br>Careers</div>
<div class="foot-sep abs" style="left:449px"></div>
<div class="foot-col abs" style="left:501px"><h3>FAQ</h3>Help<br>Privacy Policy<br>Terms of Service</div>
<div class="foot-sep abs" style="left:606px"></div>
<div class="foot-brand abs"><i></i>HERONVAULT</div>
<div class="copyright abs">Copyright © 2013 Heronvault<br>All Rights Reserved.</div>

</body>
</html>
```